Menu Design Project

My Restaurant is called The Pita Corner, it's fast food restaurant serves Gyro, Wings, Subs, Fried Seafood and chicken tenders. I'm looking for a menu design to fit the fast food category and have some photos of the food on the front page as well inside the menu. I will attached some photos and you can add any other photo related to the menu from the web.

Industry/Entity Type

Restaurant

```html
<!DOCTYPE html>
<html lang="en">
<head>
<meta charset="utf-8">
<title>The Pita Corner – Menu</title>
<link rel="stylesheet" href="https://fonts.googleapis.com/css2?family=Montserrat:wght@600;700&family=Open+Sans:wght@400;600;700&family=Oswald:wght@400;500&family=Great+Vibes&display=swap">
<style>
  :root{
    --red:#e3141b;
    --red-dark:#c40c12;
    --ink:#1d1d1d;
    --paper:#ffffff;
    --backdrop:#e9e9ea;
    --photo-warm:#d88a3e;
    --photo-grey:#b9bcc0;
  }
  *{box-sizing:border-box;margin:0;padding:0}
  html,body{width:1200px;height:770px;overflow:hidden;background:var(--backdrop)}
  body{position:relative;font-family:"Open Sans",Arial,sans-serif;color:var(--ink)}
  .panel{position:absolute;width:570px;height:355px;background:var(--paper);box-shadow:0 2px 6px rgba(0,0,0,.18);overflow:hidden}
  .panel--back{left:20px;top:20px}
  .panel--front{left:20px;top:395px}
  .panel--menu-top{left:610px;top:20px}
  .panel--menu-bottom{left:610px;top:395px}
  .frame{position:absolute;inset:9px;border:2px solid var(--red);pointer-events:none}
  .abs{position:absolute}

  .tab{position:absolute;height:18px;background:var(--red);color:#fff;font-family:"Montserrat",Arial,sans-serif;font-weight:700;font-size:11px;letter-spacing:.06em;text-transform:uppercase;display:flex;align-items:center;gap:6px;padding:0 10px}
  .tab .dot{width:9px;height:9px;border-radius:50%;border:1.5px solid #fff;flex:none}
  .tab small{font-size:7px;letter-spacing:.04em}

  .list{position:absolute;list-style:none;font-size:9.5px;line-height:15px}
  .list li{display:flex;justify-content:space-between}
  .note{position:absolute;color:var(--red);font-size:9.5px;text-transform:uppercase}
  .extra{color:var(--red);font-size:6.5px;text-transform:uppercase;margin-left:4px}

  .photo{position:absolute;border-radius:10px}
  .photo--wings{background:radial-gradient(circle at 50% 50%,#c8652a,#e6a25a 60%,transparent 72%)}
  .photo--burger{background:radial-gradient(ellipse at 50% 50%,#a8621f,#d99a46 55%,#6aa84f 62%,transparent 72%)}
  .photo--gyro{background:radial-gradient(ellipse at 50% 50%,#7a5233,#e9cc96 60%,transparent 72%)}
  .photo--combo{background:radial-gradient(ellipse at 50% 55%,#e4b041,#c9332b 55%,transparent 72%)}
  .photo--cans{background:linear-gradient(90deg,#c7202a,#2e8f3f 35%,#f08a1d 65%,#b51e2a)}
  .photo--map{background:linear-gradient(135deg,#d7d9dc,#bfc2c6);border:2px solid #9a9da1;border-radius:16px}
  .photo--plate{background:linear-gradient(180deg,#f3b7b9,#ffffff 50%,#f3b7b9);opacity:.85;border-radius:4px}

  .brand{display:flex;align-items:center;gap:6px;font-family:"Montserrat",Arial,sans-serif;font-weight:700;color:var(--ink)}
  .brand .mark{width:12px;height:12px;border-radius:50%;background:var(--red);flex:none}

  /* back panel */
  .band{position:absolute;left:11px;right:11px;height:36px;background:var(--red);display:flex;align-items:center;justify-content:center}
  .band--tagline{top:11px;font-family:"Great Vibes",cursive;color:#fff;font-size:24px}
  .drinks-list{position:absolute;left:28px;top:86px;width:140px;font-size:10px;line-height:14px}
  .callout{position:absolute;left:190px;top:185px;width:150px;text-align:center;font-size:9px}
  .callout strong{display:block;color:var(--red);font-size:12px;font-style:italic;margin-top:3px}
  .hours{position:absolute;font-size:10px;text-align:center}
  .hours em{display:block;color:var(--red);font-style:italic}
  .contact-line{position:absolute;left:30px;right:30px;bottom:22px;border-top:1.5px solid #555;padding-top:6px;display:flex;justify-content:space-between;font-family:"Montserrat",Arial,sans-serif;font-size:11px;font-weight:600}
  .contact-line span{display:flex;align-items:center;gap:6px}

  /* front panel */
  .side-strip{position:absolute;left:11px;top:20px;width:78px;height:155px;background:var(--red)}
  .side-strip .photo--plate{left:12px;top:10px;width:54px;height:135px}
  .front-name{position:absolute;left:200px;top:28px;font-size:14px}
  .front-title{position:absolute;left:130px;top:72px;font-family:"Oswald",Arial,sans-serif;font-size:27px;color:var(--red);letter-spacing:.01em}
  .front-hours{position:absolute;left:180px;top:122px;width:160px;text-align:center;font-size:10px}
  .front-hours b{display:block;color:var(--red);font-family:"Oswald",Arial,sans-serif;font-weight:500;font-size:11px;margin-top:4px}
  .band--address{bottom:11px;height:28px;justify-content:space-around;color:#fff;font-family:"Montserrat",Arial,sans-serif;font-weight:600;font-size:12px}
  .band--address span{display:flex;align-items:center;gap:6px}

  .menu-title{position:absolute;left:0;right:0;top:38px;display:flex;justify-content:center;color:var(--red);font-size:12px}
  .menu-title .brand{color:var(--red);font-family:"Open Sans",Arial,sans-serif;font-weight:600}
  .menu-logo{position:absolute;left:277px;top:16px;width:18px;height:18px;border-radius:50%;background:var(--red)}
</style>
</head>
<body>

<!-- Outside: back panel -->
<section class="panel panel--back">
  <div class="frame"></div>
  <div class="band band--tagline">Good Food, Good Mood</div>
  <div class="tab" style="left:26px;top:60px"><span class="dot"></span>Drinks</div>
  <p class="drinks-list">Cola, Diet Cola,<br>Lemon-Lime Soda, Sports Drink,<br>Orange Soda,<br>Strawberry Soda,<br>Pepper Soda and more.</p>
  <div class="photo photo--cans" role="img" aria-label="Photo of assorted soda cans" style="left:185px;top:80px;width:110px;height:65px"></div>
  <div class="abs" style="left:252px;top:160px;width:22px;height:22px;border-radius:50%;background:var(--red)"></div>
  <p class="callout">Call Us for Pick Up orders or Catering<strong>713-555-0148</strong></p>
  <div class="photo photo--map" role="img" aria-label="Street map showing the restaurant location" style="left:365px;top:60px;width:180px;height:130px"></div>
  <p class="hours" style="left:365px;top:200px;width:180px">Hours of operation:<em>Monday to Sunday 11am-9pm</em></p>
  <div class="contact-line">
    <span>
      <svg width="10" height="12" viewBox="0 0 10 12"><path d="M5 0a4 4 0 0 0-4 4c0 3 4 8 4 8s4-5 4-8a4 4 0 0 0-4-4z" fill="var(--red)"/><circle cx="5" cy="4" r="1.5" fill="#fff"/></svg>
      4120 Cedar Grove Ave, Houston, TX 77045
    </span>
    <span>
      <svg width="11" height="11" viewBox="0 0 12 12"><circle cx="6" cy="6" r="5.3" fill="none" stroke="var(--red)" stroke-width="1.2"/><path d="M4 3.3l1 1.4-.6.7a4 4 0 0 0 2.2 2.2l.7-.6 1.4 1-.6 1c-2.5-.3-4.4-2.2-4.7-4.7z" fill="var(--red)"/></svg>
      713-555-0148
    </span>
  </div>
</section>

<!-- Outside: front cover -->
<section class="panel panel--front">
  <div class="frame"></div>
  <div class="side-strip"><div class="photo photo--plate" role="img" aria-label="Plate and cutlery illustration"></div></div>
  <div class="front-name brand"><span class="mark"></span>The Pita Corner</div>
  <h1 class="front-title">The Pita Corner Restaurant</h1>
  <p class="front-hours">Hours of operation:<b>Monday to Sunday 11am-9pm</b></p>
  <div class="photo photo--wings" role="img" aria-label="Photo of chicken wings" style="left:30px;top:185px;width:140px;height:105px"></div>
  <div class="photo photo--burger" role="img" aria-label="Photo of a burger" style="left:215px;top:180px;width:140px;height:115px"></div>
  <div class="photo photo--gyro" role="img" aria-label="Photo of a gyro wrap" style="left:390px;top:175px;width:160px;height:120px"></div>
  <div class="band band--address">
    <span>
      <svg width="10" height="12" viewBox="0 0 10 12"><path d="M5 0a4 4 0 0 0-4 4c0 3 4 8 4 8s4-5 4-8a4 4 0 0 0-4-4z" fill="#fff"/><circle cx="5" cy="4" r="1.5" fill="var(--red)"/></svg>
      4120 Cedar Grove Ave, Houston, TX 77045
    </span>
    <span>
      <svg width="12" height="12" viewBox="0 0 12 12"><circle cx="6" cy="6" r="5.3" fill="none" stroke="#fff" stroke-width="1.2"/><path d="M4 3.3l1 1.4-.6.7a4 4 0 0 0 2.2 2.2l.7-.6 1.4 1-.6 1c-2.5-.3-4.4-2.2-4.7-4.7z" fill="#fff"/></svg>
      713-555-0148
    </span>
  </div>
</section>

<!-- Inside: upper panel -->
<section class="panel panel--menu-top">
  <div class="frame"></div>
  <div class="menu-logo"></div>
  <div class="menu-title"><span class="brand">The Pita Corner Menu</span></div>

  <div class="tab" style="left:11px;top:78px;width:110px"><span class="dot"></span>Chicken</div>
  <ul class="list" style="left:30px;top:102px;width:200px">
    <li><span>10 Large Wings</span><span>$8.99</span></li>
    <li><span>20 Large Wings</span><span>$16.99</span></li>
    <li><span>30 Large Wings</span><span>$23.99</span></li>
    <li><span>50 Large Wings</span><span>$39.99</span></li>
    <li><span>½ lb. Chicken Strips</span><span>$5.49</span></li>
    <li><span>1lb. Chicken Strips</span><span>$7.99</span></li>
    <li><span>½ lb. Gizzards</span><span>$5.49</span></li>
    <li><span>1lb. Gizzards</span><span>$7.99</span></li>
  </ul>

  <div class="tab" style="left:30px;top:230px;width:110px"><span class="dot"></span>Seafood</div>
  <ul class="list" style="left:40px;top:254px;width:190px">
    <li><span>½ lb. Shrimp</span><span>$7.99</span></li>
    <li><span>1lb. Shrimp</span><span>$13.99</span></li>
    <li><span>½ lb. Fish</span><span>$6.99</span></li>
    <li><span>1lb. Fish</span><span>$12.99</span></li>
  </ul>

  <div class="tab" style="right:11px;top:78px;width:150px;justify-content:flex-end">Fresh Salad<span class="dot"></span></div>
  <ul class="list" style="left:270px;top:102px;width:270px">
    <li><span>Caesar Salad</span><span>$4.95</span></li>
    <li><span>Gyro Salad</span><span>$5.95</span></li>
    <li><span>Shrimp Caesar Salad</span><span>$6.25</span></li>
    <li><span>Greek Salad</span><span>$5.95</span></li>
  </ul>

  <div class="tab" style="right:11px;top:172px;width:150px;justify-content:flex-end">Gyro &amp; Subs<span class="dot"></span></div>
  <ul class="list" style="left:270px;top:196px;width:270px">
    <li><span>Gyro (Original or Chicken)</span><span>$6.99</span></li>
    <li><span>¼ lb. Black Angus Burger</span><span>$3.99</span></li>
    <li><span>Buffalo Chicken Sandwich</span><span>$5.99</span></li>
  </ul>
  <p class="note" style="left:270px;top:244px">Your choice of 6" or footlong subs</p>
  <ul class="list" style="left:270px;top:260px;width:270px">
    <li><span>Po Boy Shrimp</span><span>$7.55-$9.25</span></li>
    <li><span>Philly (Steak or Chicken)</span><span>$6.75-$8.99</span></li>
    <li><span>Fish</span><span>$6.75-$8.99</span></li>
    <li><span>Turkey &amp; Cheese</span><span>$6.49-$7.95</span></li>
  </ul>
</section>

<!-- Inside: lower panel -->
<section class="panel panel--menu-bottom">
  <div class="frame"></div>
  <div class="tab" style="left:11px;top:20px;width:110px"><span class="dot"></span>Sides</div>
  <ul class="list" style="left:30px;top:44px;width:190px">
    <li><span>French Fries</span><span>$2.79</span></li>
    <li><span>Cajun Fries</span><span>$3.99</span></li>
    <li><span>Onion Rings</span><span>$4.99</span></li>
    <li><span>5 Jalapeno Poppers</span><span>$4.99</span></li>
    <li><span>Fried Okra</span><span>$4.99</span></li>
    <li><span>Fried Mushroom</span><span>$5.49</span></li>
    <li><span>5 Mozzarella Sticks</span><span>$5.49</span></li>
  </ul>

  <div class="tab" style="right:11px;top:20px;width:290px;justify-content:flex-end">Combos <small>includes 16oz soft drink!</small><span class="dot"></span></div>
  <ul class="list" style="left:250px;top:44px;width:290px">
    <li><span>½ lb. Fish &amp; Fries</span><span>$9.99</span></li>
    <li><span>½ lb. Shrimp &amp; Fries</span><span>$10.99</span></li>
    <li><span>6" Philly (Steak or Chicken) &amp; Fries</span><span>$9.99</span></li>
    <li><span>Gyro (Original, Chicken or Fish) &amp; Fries</span><span>$9.49</span></li>
    <li><span>5 Wings &amp; Fries</span><span>$9.49</span></li>
    <li><span>½ lb. Gizzards &amp; Fries</span><span>$7.99</span></li>
    <li><span>¼ lb. Black Angus Burger &amp; Fries</span><span>$6.99<span class="extra">*cheese extra</span></span></li>
    <li><span>5 Wings &amp; Gizzards</span><span>$11.49</span></li>
    <li><span>½ lb. Chicken Strips &amp; Fries</span><span>$7.99</span></li>
  </ul>

  <div class="tab" style="left:215px;top:200px;width:120px"><span class="dot"></span>Kids Meal</div>
  <ul class="list" style="left:200px;top:224px;width:230px">
    <li><span>Chicken Nuggets 4pc with small drink and fries</span><span style="color:var(--red);font-weight:700">$4.95</span></li>
    <li><span>Chicken Strips 2pc with small drink and fries</span><span style="color:var(--red);font-weight:700">$4.95</span></li>
    <li><span>Mac &amp; Cheese</span><span style="color:var(--red);font-weight:700">$3.95</span></li>
  </ul>

  <div class="photo photo--combo" role="img" aria-label="Photo of nuggets, burger, fries and a soda cup" style="left:22px;top:185px;width:165px;height:140px"></div>
  <div class="photo photo--combo" role="img" aria-label="Photo of chicken strips, fries and a soda cup" style="left:440px;top:205px;width:115px;height:125px"></div>
</section>

</body>
</html>
```